Business Card Design - Brightfold Dwellings

Hi there,

We would like a business card for our new venture, Brightfold Dwellings.

We are based in Western Australia and specialise in taking tired, old properties and making them look new again. We aim to create enjoyably liveable homes for young families in particular.

Product pricing is mid range i.e. appliances, furnishings, fixtures (not top end but not cheap either)

Our work is primarily cosmetic renovation (approx. 80%) and the rest construction (approx 20%).

We would like a business card that conveys the following:
- clean, simplistic/minimalistic design
- modern, contemporary style
- a touch of funk/uniqueness
- appealing to both females and males
- professionalism

I have uploaded our logo in grey or green, I do not mind which one you choose to use (please use either coloured logo on the pure white background not the white on colour version).

Details to include on the business card are:
Names: Corina Maddox and Pete Okonbrie
Mobile: 0417 362 908
Email: info@brightfolddwellings.com.au
Website: www.brightfolddwellings.com.au (note: this website is currently being developed)
Note: We will provide final details such as mobile number and names on on selection of successful design)

On the other side of the card please include a line similar to "We buy tired, un-renovated properties and sell them looking new again!"

The business card will also need to include the following "ABN 47 219 635 104" which is our Australian Business Number (again the actual number will be provided on selection of successful design). We would like this number somewhere near our name Brightfold Dwellings but in much smaller text.

The purpose of the business cards will be to give to suppliers, real estate agents, people wanting assistance in locating a property in need of renovation and potential buyers.

Thank you and please let me know if you have any further questions.

```html
<!DOCTYPE html>
<html lang="en">
<head>
<meta charset="utf-8">
<title>Brightfold Dwellings – Business Card</title>
<link rel="stylesheet" href="https://fonts.googleapis.com/css2?family=Source+Sans+3:wght@400;600&display=swap">
<style>
  :root {
    --backdrop: #b9b9b9;
    --card: #f4f4f4;
    --card-edge: #e2e2e2;
    --green: #8cc63f;
    --ink: #2b2b2b;
    --muted: #555555;
    --font: "Source Sans 3", "Myriad Pro", sans-serif;
  }
  * { box-sizing: border-box; margin: 0; padding: 0; }
  html, body { width: 1200px; height: 900px; overflow: hidden; }
  body {
    background: radial-gradient(ellipse at 50% 45%, #d6d6d6 0%, var(--backdrop) 100%);
    font-family: var(--font);
    color: var(--ink);
    position: relative;
  }
  .card {
    position: absolute;
    left: 330px;
    width: 540px;
    height: 330px;
    background: linear-gradient(135deg, #ffffff 0%, var(--card) 60%, var(--card-edge) 100%);
    box-shadow: 0 10px 30px rgba(0,0,0,0.22);
  }
  .card--back { top: 90px; }
  .card--front { top: 480px; }

  /* back side */
  .back-band {
    position: absolute;
    left: 40px; right: 40px; top: 70px; bottom: 60px;
    background: radial-gradient(ellipse at center, #ffffff 0%, rgba(255,255,255,0) 75%);
  }
  .brand {
    display: flex;
    align-items: center;
    gap: 10px;
    color: var(--green);
    font-weight: 400;
    letter-spacing: -0.5px;
  }
  .brand-dot {
    width: 14px; height: 14px;
    border-radius: 50%;
    background: var(--green);
    flex: none;
  }
  .card--back .brand {
    position: absolute;
    top: 118px; left: 0; right: 0;
    justify-content: center;
    font-size: 40px;
  }
  .tagline {
    position: absolute;
    top: 196px; left: 0; right: 0;
    text-align: center;
    font-size: 13px;
    line-height: 1.45;
    color: var(--ink);
  }
  .tagline .accent { color: var(--green); font-size: 14px; }

  /* front side */
  .front-info {
    position: absolute;
    left: 40px; top: 120px;
  }
  .card--front .brand { font-size: 30px; }
  .abn {
    font-size: 9px;
    letter-spacing: 0.5px;
    color: var(--muted);
    margin: 2px 0 0 24px;
  }
  .names {
    margin-top: 20px;
    font-size: 14px;
    letter-spacing: 0.5px;
    text-transform: uppercase;
    display: flex;
    align-items: center;
    gap: 10px;
  }
  .names .divider {
    width: 2px; height: 16px;
    background: var(--green);
  }
  .contacts {
    margin-top: 18px;
    display: grid;
    grid-template-columns: 46px auto;
    row-gap: 2px;
    align-items: baseline;
    font-size: 13px;
  }
  .contacts dt {
    font-size: 7px;
    letter-spacing: 0.6px;
    text-transform: uppercase;
    color: var(--green);
  }
  .contacts dd { color: var(--ink); }
</style>
</head>
<body>
  <section class="card card--back" aria-label="Card back">
    <div class="back-band"></div>
    <div class="brand"><span class="brand-dot"></span>Brightfold Dwellings</div>
    <p class="tagline">We buy tired, un-renovated properties and sell them<br><span class="accent">looking new again!</span></p>
  </section>

  <section class="card card--front" aria-label="Card front">
    <div class="front-info">
      <div class="brand"><span class="brand-dot"></span>Brightfold Dwellings</div>
      <p class="abn">ABN 47 219 635 104</p>
      <p class="names"><span>Corina Maddox</span><span class="divider"></span><span>Pete Okonbrie</span></p>
      <dl class="contacts">
        <dt>Mobile</dt><dd>0417 362 908</dd>
        <dt>Email</dt><dd>info@brightfolddwellings.com.au</dd>
        <dt>Website</dt><dd>www.brightfolddwellings.com.au</dd>
      </dl>
    </div>
  </section>
</body>
</html>
```